Massage Therapy and Personal Training Business Card (Lorvex Wellness)

I need a logo design based in Washington. The company is called Lorvex Wellness. Lorvex are my initials. I specialize in massage therapy and personal training and general wellness of my clients. I've tried getting designs but haven't quite yet found what I'm looking for. I'm not inclined to a certain color yet but some color that resembles wellness such as light blue and white or green and white. Again, I'm not really picky about that. Thank you in advance

Industry/Entity Type

Business

Contact Information for Business Card

Have the description on one side and space for writing information on the back side such as number, appt, etc. I have an example attached. I see a lot of these card. I dont want the exact one, but something similar. Simple, professional and elegant.

Colors

Designer to choose colors to be used in the design.

Requirements
Must have
• Space on the back side to write
• A professional, elegant look
Should not have
• cartoon like style.

```html
<!DOCTYPE html>
<html lang="en">
<head>
<meta charset="utf-8">
<title>Lorvex Wellness – Business Card</title>
<link href="https://fonts.googleapis.com/css2?family=Quicksand:wght@500;600&family=Open+Sans:wght@400&display=swap" rel="stylesheet">
<style>
  :root {
    --backdrop: #e4e6e8;
    --card: #ffffff;
    --brand-blue: #1aa3e0;
    --brand-green: #6cbd45;
    --text-grey: #8a8d90;
    --rule: #c9cbcd;
    --figure-light: #d4d6d8;
    --figure-dark: #8d9094;
  }
  * { margin: 0; padding: 0; box-sizing: border-box; }
  html, body {
    width: 1200px;
    height: 873px;
    overflow: hidden;
    background: var(--backdrop);
  }
  .sheet {
    width: 1200px;
    height: 873px;
    display: flex;
    align-items: center;
    justify-content: center;
    gap: 44px;
  }
  .card {
    position: relative;
    width: 540px;
    height: 310px;
    background: var(--card);
    border-radius: 18px;
    overflow: hidden;
    box-shadow: 0 6px 20px rgba(0,0,0,0.12);
  }
  .wordmark {
    font-family: "Quicksand", sans-serif;
    font-weight: 600;
    color: var(--brand-blue);
    font-size: 40px;
    line-height: 1;
    display: flex;
    align-items: center;
    gap: 10px;
    white-space: nowrap;
  }
  .wordmark-dot {
    width: 12px;
    height: 12px;
    border-radius: 50%;
    background: var(--brand-green);
    flex: none;
  }
  .tagline {
    font-family: "Open Sans", sans-serif;
    font-size: 11.5px;
    color: var(--text-grey);
    margin-top: 6px;
    white-space: nowrap;
  }
  /* Logo side */
  .card--logo .brand {
    position: absolute;
    left: 40px;
    top: 70px;
  }
  /* Contact side */
  .anatomy {
    position: absolute;
    left: 0;
    top: 0;
    width: 190px;
    height: 100%;
    background: linear-gradient(180deg, var(--figure-light) 0%, #b8babd 45%, var(--figure-dark) 100%);
  }
  .card--contact .brand {
    position: absolute;
    left: 212px;
    top: 40px;
  }
  .card--contact .wordmark { font-size: 34px; }
  .card--contact .tagline { font-size: 10px; }
  .rule {
    position: absolute;
    left: 212px;
    right: 26px;
    height: 1px;
    background: var(--rule);
  }
  .rule--top { top: 146px; }
  .rule--bottom { top: 222px; }
  .person-name {
    position: absolute;
    left: 212px;
    top: 182px;
    font-family: "Quicksand", sans-serif;
    font-weight: 500;
    font-size: 24px;
    color: var(--brand-blue);
  }
  .contact-line {
    position: absolute;
    display: flex;
    align-items: center;
    gap: 7px;
    font-family: "Quicksand", sans-serif;
    font-weight: 500;
    font-size: 14px;
    color: var(--brand-blue);
    white-space: nowrap;
  }
  .contact-line--phone { right: 26px; top: 160px; }
  .contact-line--email { left: 212px; top: 236px; }
  .contact-icon { width: 22px; height: 22px; flex: none; }
</style>
</head>
<body>
<main class="sheet">
  <section class="card card--logo" aria-label="Card logo side">
    <div class="brand">
      <div class="wordmark"><span class="wordmark-dot"></span>Lorvex Wellness</div>
      <p class="tagline">Massage therapy • Personal training • General wellness</p>
    </div>
  </section>

  <section class="card card--contact" aria-label="Card contact side">
    <div class="anatomy" role="img" aria-label="Anatomical illustration of back and shoulder muscles with highlighted joints"></div>

    <div class="brand">
      <div class="wordmark"><span class="wordmark-dot"></span>Lorvex Wellness</div>
      <p class="tagline">Massage therapy • Personal training • General wellness</p>
    </div>

    <div class="rule rule--top"></div>
    <p class="person-name">Daniel Reyes</p>

    <p class="contact-line contact-line--phone">
      <svg class="contact-icon" viewBox="0 0 22 22" aria-hidden="true">
        <circle cx="11" cy="11" r="10" fill="var(--brand-green)"/>
        <circle cx="11" cy="11" r="7.5" fill="none" stroke="#fff" stroke-width="1.2"/>
        <path d="M8 7.2c.6-.5 1.1-.4 1.4.1l.8 1.3c.3.5.1.9-.3 1.2l-.4.3c.4 1 1.2 1.8 2.2 2.3l.3-.4c.3-.4.8-.6 1.2-.3l1.3.8c.5.3.6.8.1 1.4-.6.7-1.4.9-2.3.5-2-.9-3.6-2.5-4.5-4.5-.4-.9-.4-1.9.2-2.7z" fill="#fff"/>
      </svg>
      801-555 0173
    </p>

    <div class="rule rule--bottom"></div>

    <p class="contact-line contact-line--email">
      <svg class="contact-icon" viewBox="0 0 22 22" aria-hidden="true">
        <circle cx="11" cy="11" r="10" fill="var(--brand-green)"/>
        <circle cx="11" cy="11" r="7.5" fill="none" stroke="#fff" stroke-width="1.2"/>
        <rect x="6.5" y="8" width="9" height="6.2" rx="0.6" fill="#fff"/>
        <path d="M6.8 8.3 11 11.4l4.2-3.1" fill="none" stroke="var(--brand-green)" stroke-width="0.9"/>
      </svg>
      hello@lorvexmail.com
    </p>
  </section>
</main>
</body>
</html>
```